Business Card Design Project

Company name KD MOTOR SERVICES
KD MOTOR
name of owner: Dario Venn
Phone: 604-555-0187
Email: info@kdmotorworks.example
website: www.kdmotorworks.example
Address
24917 51 Ave Surrey, BC V5Q 8K3

Black Back round

Business

```html
<!DOCTYPE html>
<html lang="en">
<head>
<meta charset="utf-8">
<title>KD Motor Services – Business Cards</title>
<link rel="stylesheet" href="https://fonts.googleapis.com/css2?family=Nunito:wght@400;600;700&display=swap">
<style>
  :root {
    --card-black: #0d0d0d;
    --card-white: #ffffff;
    --page-bg: #e6e4e0;
    --label: #3a3a3a;
  }
  * { box-sizing: border-box; margin: 0; padding: 0; }
  html, body { width: 1200px; height: 816px; overflow: hidden; }
  body {
    background: var(--page-bg);
    font-family: "Nunito", sans-serif;
    position: relative;
  }
  .card {
    position: absolute;
    background: var(--card-black);
    color: var(--card-white);
    overflow: hidden;
    box-shadow: 0 4px 14px rgba(0,0,0,.18);
  }

  /* Front card */
  .card--front { left: 40px; top: 60px; width: 560px; height: 320px; }
  .front__band {
    position: absolute; left: 0; right: 0; top: 70px; height: 62px;
    background: var(--card-white);
  }
  .front__name {
    position: absolute; left: 0; right: 0; top: 75px;
    text-align: center; color: var(--card-black);
    font-size: 36px; font-weight: 600; line-height: 52px; letter-spacing: 1px;
  }
  .front__contact {
    position: absolute; left: 0; right: 0; top: 146px;
    text-align: center; font-size: 17px; font-weight: 600; line-height: 25px;
  }
  .strip {
    position: absolute; left: 0; right: 0; bottom: 0;
    background: var(--card-white); color: var(--card-black);
    text-align: right; font-weight: 600;
  }
  .card--front .strip { height: 30px; padding-right: 22px; font-size: 15px; line-height: 30px; }

  /* Back card */
  .card--back { left: 620px; top: 260px; width: 560px; height: 320px; }
  .back__rule {
    position: absolute; left: 0; right: 0; height: 3px; background: var(--card-white);
  }
  .back__rule--top { top: 92px; }
  .back__rule--bottom { top: 228px; }
  .back__title {
    position: absolute; left: 0; right: 0; top: 112px;
    text-align: center; font-size: 38px; font-weight: 600; line-height: 52px; letter-spacing: 1px;
  }
  .back__tagline {
    position: absolute; left: 0; right: 0; top: 170px;
    text-align: center; font-size: 19px; font-weight: 600; line-height: 26px; letter-spacing: 2px;
  }

  /* Alternate card */
  .alt-label {
    position: absolute; left: 40px; top: 470px;
    font-size: 20px; font-weight: 700; color: var(--label);
  }
  .card--alt { left: 40px; top: 510px; width: 350px; height: 200px; }
  .alt__name {
    position: absolute; left: 36px; top: 78px; font-size: 15px; font-weight: 600;
  }
  .alt__divider {
    position: absolute; left: 150px; top: 46px; width: 1.5px; height: 82px;
    background: var(--card-white);
  }
  .alt__contact {
    position: absolute; left: 164px; top: 50px; font-size: 9px; font-weight: 600; line-height: 15px;
  }
  .card--alt .strip { height: 20px; padding-right: 14px; font-size: 10px; line-height: 20px; }
</style>
</head>
<body>

  <section class="card card--front" aria-label="Business card front">
    <div class="front__band"></div>
    <h1 class="front__name">Dario Venn</h1>
    <div class="front__contact">
      <p>24917 51 Ave Surrey, BC V5Q 8K3</p>
      <p>604-555-0187</p>
      <p>info@kdmotorworks.example</p>
      <p>kdmotorworks.example</p>
    </div>
    <div class="strip">KD MOTOR SERVICES</div>
  </section>

  <section class="card card--back" aria-label="Business card back">
    <div class="back__rule back__rule--top"></div>
    <h2 class="back__title">KD MOTOR SERVICES</h2>
    <p class="back__tagline">“COMPLETE CAR CARE”</p>
    <div class="back__rule back__rule--bottom"></div>
  </section>

  <p class="alt-label">Alternate:</p>
  <section class="card card--alt" aria-label="Alternate business card front">
    <p class="alt__name">Dario Venn</p>
    <div class="alt__divider"></div>
    <div class="alt__contact">
      <p>24917 51 Ave Surrey, BC V5Q 8K3</p>
      <p>604-555-0187</p>
      <p>info@kdmotorworks.example</p>
      <p>kdmotorworks.example</p>
    </div>
    <div class="strip">KD MOTOR SERVICES</div>
  </section>

</body>
</html>
```